Career development coaching - school lever to adults, needs a business card

Tandel Grove - An independent Career Advice business that provides 1-2-1 advice,for career development, entrepreneurial support and workshops needs a business card. Our clients of all ages (school leaver to adults looking for a career move) and universities and colleges. We would like the card to be double-sided with a modern, professional look. Looking for something professional yet very creative and original. Want a standard size business card that inspires a second look because it stands out from the rest.

One side of the card to have a design incorporating the logo with Tandel Grove name with the strap line “Helping you find your future” and space for the company website

Other side of the card to the logo/Tandel Grove name and the usual contact information:
Individual Name
Job Title (for example, Director)
Phone number
Email address
Company website address

Facebook, LinkedIn and Twitter links will need to go somewhere (back or front!)

The design will be used for 3 individuals so should be editable so that we can update as needed/as we grow.

Attached is the company logo/colours to be incorporated.

Target Market(s)

1-2-1 advice,for career development, entrepreneurial support and workshops needs a business card. Our clients of all ages (school leaver to adults looking for a career move) and universities and colleges.

Industry/Entity Type

Consulting

Contact Information for Business Card

Individual Name
Phone number
Email address
Company website address

Font styles to use
Sans Serif

Colors
0255a3
3176b5
faa54b
f78f20
85acd3
cfdeed

Requirements
Must have
• use the Tandel Grove Logo in some way - using the colours and the blue/orange palette
• For the logo - hope this makes sense to someone or if they direclty relate to the logo image attached!
• For the Orange:- Pantone 1585 C
• In CMYK : C3 M71 Y100 K0
• For the Blue:- 100% Pantone 7469 C
• In CMYK : C100 M62 Y27 K7
• Please feel free to contact me with any questions for more info
Nice to have
• happy to see any creative designs
Should not have
• Nothing too traditional,

```html
<!DOCTYPE html>
<html lang="en">
<head>
<meta charset="utf-8">
<title>Tandel Grove — Business Card</title>
<link rel="stylesheet" href="https://fonts.googleapis.com/css2?family=Lato:wght@400;700&family=Oswald:wght@500&family=Roboto:wght@400&display=swap">
<style>
  :root {
    --backdrop: #3b302a;
    --card: #ffffff;
    --brand-blue: #135e8e;
    --brand-orange: #ef7733;
    --text-grey: #5f6368;
    --rule-grey: #b9b9b9;
  }
  * { margin: 0; padding: 0; box-sizing: border-box; }
  html, body { width: 1200px; height: 1000px; overflow: hidden; }
  body { background: var(--backdrop); position: relative; font-family: "Lato", sans-serif; }

  .card {
    position: absolute;
    left: 287px;
    width: 627px;
    height: 358px;
    background: var(--card);
    border-radius: 28px;
  }
  .card--front { top: 140px; }
  .card--back { top: 531px; }

  .brand-dot { position: absolute; border-radius: 50%; background: var(--brand-orange); }
  .wordmark {
    position: absolute;
    font-family: "Lato", sans-serif;
    font-weight: 700;
    font-variant: small-caps;
    color: var(--brand-blue);
    letter-spacing: 1.5px;
    white-space: nowrap;
    line-height: 1;
  }

  /* front */
  .card--front .brand-dot { width: 100px; height: 100px; left: 263px; top: 65px; }
  .card--front .wordmark { font-size: 40px; left: 0; width: 100%; text-align: center; top: 200px; }
  .tagline {
    position: absolute; top: 243px; left: 0; width: 100%; text-align: center;
    font-family: "Roboto", sans-serif; font-size: 16px; letter-spacing: 2px; color: var(--text-grey);
  }
  .visit {
    position: absolute; top: 312px; left: 0; width: 100%; text-align: center;
    font-family: "Roboto", sans-serif; font-size: 15px; color: var(--text-grey);
  }

  /* back */
  .card--back .brand-dot { width: 64px; height: 64px; left: 135px; top: 84px; }
  .card--back .wordmark { font-size: 40px; left: 214px; top: 96px; }

  .person { position: absolute; right: 356px; top: 214px; text-align: right; }
  .person__name {
    font-family: "Oswald", sans-serif; font-weight: 500; font-size: 24px;
    color: var(--brand-blue); letter-spacing: 0.5px; line-height: 1.2;
  }
  .person__role { font-size: 15px; color: var(--text-grey); margin-top: 1px; }

  .divider { position: absolute; left: 288px; top: 212px; width: 1px; height: 52px; background: var(--rule-grey); }

  .contacts { position: absolute; left: 306px; top: 208px; list-style: none; }
  .contacts li {
    display: flex; align-items: center; gap: 5px;
    font-size: 15px; color: var(--text-grey); height: 20px;
  }
  .contacts svg { width: 11px; height: 11px; fill: var(--brand-orange); flex: none; }

  .social { position: absolute; left: 261px; top: 290px; display: flex; gap: 8px; }
  .social span { width: 13px; height: 13px; border: 1px solid #6d6d6d; border-radius: 2px; display: block; }
</style>
</head>
<body>

<section class="card card--front">
  <span class="brand-dot"></span>
  <div class="wordmark">Tandel Grove</div>
  <p class="tagline">Guiding you to what comes next</p>
  <p class="visit">Visit us: www.TandelGrove.com</p>
</section>

<section class="card card--back">
  <span class="brand-dot"></span>
  <div class="wordmark">Tandel Grove</div>

  <div class="person">
    <div class="person__name">MARA ELLISON</div>
    <div class="person__role">Director</div>
  </div>
  <span class="divider"></span>

  <ul class="contacts">
    <li>
      <svg viewBox="0 0 24 24" aria-hidden="true"><path d="M6.6 10.8a15.1 15.1 0 0 0 6.6 6.6l2.2-2.2a1 1 0 0 1 1-.25 11.4 11.4 0 0 0 3.6.57 1 1 0 0 1 1 1V20a1 1 0 0 1-1 1A17 17 0 0 1 3 4a1 1 0 0 1 1-1h3.5a1 1 0 0 1 1 1c0 1.25.2 2.45.57 3.6a1 1 0 0 1-.25 1z"/></svg>
      555-0142-7730
    </li>
    <li>
      <svg viewBox="0 0 24 24" aria-hidden="true"><path d="M2 5h20v14H2z M2 5l10 8 10-8" /></svg>
      info@tandelgrove.com
    </li>
    <li>
      <svg viewBox="0 0 24 24" aria-hidden="true"><circle cx="12" cy="12" r="10"/></svg>
      www.tandelgrove.com
    </li>
  </ul>

  <div class="social" aria-label="Social links">
    <span></span><span></span><span></span>
  </div>
</section>

</body>
</html>
```